New Business Card Design Project

Hi,

I'd like to create a logo for my business www.tellwickandtide.com. You will need to download two fonts for the business card: Lobster & Noticia Text. The fonts are free to download. No logo required.

Potential design idea:
One side hot pink (white font), one side white (grey font)
- On one side, hot pink similar to the pink on the website.
- Show tellwick + tide plus "your never-ending closet" in white font
- We really need it to be sleek, minimalistic and bright
- On the other side, we need to show our instagram and facebook URLs (fb.com/tellwickandtide, instagram.com/tellwickandtide). Please use the same dark grey font as our website and use a hollowed out grey FB & Instagram logo
We also need to show the following details, website, space for name and email (hello@tellwickandtide.com).

Feel free to go as creative as you would like! The above is a safe template that we know will satisfy our needs. Aim is to minimalist, simple and bold. , Details for my new Business Card Design Project will be added soon.

• Needs to fit the prell.com luxe business card template.

```html
<!DOCTYPE html>
<html lang="en">
<head>
<meta charset="utf-8">
<title>Tellwick+Tide Business Card</title>
<link rel="stylesheet" href="https://fonts.googleapis.com/css2?family=Hind:wght@400;600&display=swap">
<style>
  :root {
    --hot-pink: #e5237f;
    --soft-pink: #f29bc3;
    --blush: #fce3ee;
    --paper: #ffffff;
    --ink-grey: #5b5b5d;
    --frame: #000000;
  }
  html, body {
    margin: 0;
    padding: 0;
    width: 1200px;
    height: 1000px;
    overflow: hidden;
    background: var(--paper);
  }
  .canvas {
    position: relative;
    width: 1200px;
    height: 1000px;
    font-family: "Hind", Arial, sans-serif;
  }
  .card {
    position: absolute;
    left: 106px;
    top: 81px;
    width: 995px;
    height: 607px;
    border: 15px solid var(--frame);
    background: linear-gradient(90deg,
      var(--hot-pink) 2%,
      #ee6ea6 22%,
      var(--soft-pink) 38%,
      var(--blush) 48%,
      var(--paper) 54%);
    overflow: hidden;
  }
  .brand-name {
    position: absolute;
    left: 20px;
    top: 0px;
    margin: 0;
    font-size: 100px;
    font-weight: 600;
    line-height: 1;
    color: var(--ink-grey);
    letter-spacing: 1px;
    white-space: nowrap;
  }
  .tagline {
    position: absolute;
    left: 99px;
    top: 98px;
    margin: 0;
    font-size: 52px;
    font-weight: 400;
    line-height: 1;
    white-space: nowrap;
  }
  .tagline .light { color: var(--paper); }
  .tagline .accent { color: var(--hot-pink); }
  .details {
    position: absolute;
    right: 14px;
    top: 318px;
    margin: 0;
    text-align: right;
    font-size: 52px;
    font-weight: 400;
    line-height: 62px;
    color: var(--ink-grey);
  }
  .email {
    position: absolute;
    right: 16px;
    top: 544px;
    margin: 0;
    font-size: 52px;
    line-height: 1;
    color: var(--ink-grey);
    white-space: nowrap;
  }
</style>
</head>
<body>
<div class="canvas">
  <section class="card">
    <h1 class="brand-name">Tellwick+Tide</h1>
    <p class="tagline"><span class="light">Your never</span> <span class="accent">ending closet</span></p>
    <p class="details">Name<br>Website<br>Deatils</p>
    <p class="email">hello@tellwickandtide</p>
  </section>
</div>
</body>
</html>
```